I need the following on my business card:
- Name: Dana Whitcomb
- License # 0M93216
- Title: Producer
- Phone: (555) 017-3904
- Email: Dana@CorbelInsuranceServices.com

- Company: Corbel Insurance Services
- Address: 27408 Larkmoor Ave Suite 610, Sherman Oaks, CA 90217
- Website: www.CorbelInsuranceServices.com

Also add our slogan on the card: "Steady Cover, Honest Advice"

```html
<!DOCTYPE html>
<html lang="en">
<head>
<meta charset="utf-8">
<title>Corbel Insurance Services — Business Card</title>
<link rel="stylesheet" href="https://fonts.googleapis.com/css2?family=Tinos:wght@400;700&display=swap">
<style>
  :root {
    --canvas: #ebebeb;
    --paper: #ffffff;
    --navy: #1f2b6e;
    --green: #169a48;
    --green-deep: #1c7f45;
    --blue-band: #27397a;
    --ink: #1a1a1a;
  }
  * { box-sizing: border-box; margin: 0; padding: 0; }
  html, body {
    width: 1200px; height: 1200px; overflow: hidden;
    background: var(--canvas);
    font-family: "Tinos", "Times New Roman", serif;
  }
  .sheet {
    position: relative; width: 1200px; height: 1200px;
    display: flex; align-items: center; justify-content: center; gap: 24px;
  }
  .card {
    position: relative; width: 560px; height: 320px;
    border-radius: 14px; overflow: hidden;
  }
  .card--front {
    background:
      radial-gradient(ellipse 55% 60% at 30% 45%, #2aa556 0%, rgba(42,165,86,0) 70%),
      linear-gradient(100deg, var(--green-deep) 0%, #22964f 55%, #1f5a73 68%, var(--blue-band) 78%, #23367a 100%);
  }
  .front-brand {
    position: absolute; left: 0; right: 0; top: 148px;
    text-align: center; color: #ffffff;
    font-size: 30px; font-weight: 700; letter-spacing: 1px;
  }
  .card--back { background: var(--paper); border: 1px solid #dcdcdc; }
  .person { position: absolute; left: 31px; top: 62px; }
  .person__name { color: var(--navy); font-size: 19px; font-weight: 700; line-height: 1; }
  .person__title { color: var(--ink); font-size: 10px; margin-top: 4px; }
  .address {
    position: absolute; left: 31px; top: 148px;
    font-size: 12.5px; line-height: 16px; color: var(--ink); font-style: normal;
  }
  .contacts {
    position: absolute; left: 31px; top: 218px;
    list-style: none; font-size: 12.5px; line-height: 16px; color: var(--ink);
  }
  .contacts li { display: flex; align-items: center; gap: 6px; }
  .contacts svg { width: 10px; height: 10px; flex: none; }
  .back-brand {
    position: absolute; right: 32px; top: 66px;
    color: var(--navy); font-size: 19px; font-weight: 700;
  }
  .slogan {
    position: absolute; right: 24px; top: 242px;
    color: var(--green); font-size: 13px;
  }
  .band { position: absolute; bottom: 0; height: 20px; width: 181px; }
  .band--green { left: 91px; background: var(--green); }
  .band--blue { left: 285px; background: var(--blue-band); }
</style>
</head>
<body>
<main class="sheet">
  <section class="card card--front" role="img" aria-label="Front of card: green and navy watercolour wash background with the company name">
    <div class="front-brand">Corbel Insurance Services</div>
  </section>

  <section class="card card--back">
    <div class="person">
      <div class="person__name">Dana Whitcomb</div>
      <div class="person__title">Producer</div>
    </div>
    <div class="back-brand">Corbel Insurance Services</div>
    <address class="address">
      27408 Larkmoor Ave Suite 610,<br>
      Sherman Oaks, CA 90217.<br>
      License: # 0M93216
    </address>
    <ul class="contacts">
      <li>
        <svg viewBox="0 0 10 10" aria-hidden="true"><path d="M2 1 L4 3 L3 4 Q4 6 6 7 L7 6 L9 8 L8 9.5 Q3 9 0.5 2 Z" fill="var(--navy)"/></svg>
        (555) 017-3904
      </li>
      <li>
        <svg viewBox="0 0 10 10" aria-hidden="true"><rect x="0.5" y="2" width="9" height="6.5" fill="var(--navy)"/><path d="M0.8 2.3 L5 5.6 L9.2 2.3" stroke="#fff" stroke-width="0.9" fill="none"/></svg>
        Dana@CorbelInsuranceServices.com
      </li>
      <li>
        <svg viewBox="0 0 10 10" aria-hidden="true"><circle cx="5" cy="5" r="4.5" fill="var(--navy)"/><path d="M0.8 5 H9.2 M5 0.8 Q2.5 5 5 9.2 M5 0.8 Q7.5 5 5 9.2" stroke="#fff" stroke-width="0.7" fill="none"/></svg>
        www.CorbelInsuranceServices.com
      </li>
    </ul>
    <div class="slogan">Steady Cover, Honest Advice</div>
    <div class="band band--green"></div>
    <div class="band band--blue"></div>
  </section>
</main>
</body>
</html>
```